Business cards design on a high standard

We advise clients on insurance and financial matters, since these clients pay for our advice, the design should have a high standard. Our logo should be included. From the colors we are open for everything.

Colors

Designer to choose colors to be used in the design.

```html
<!DOCTYPE html>
<html lang="en">
<head>
<meta charset="utf-8">
<title>Alpine Counsel – Business Cards</title>
<link rel="stylesheet" href="https://fonts.googleapis.com/css2?family=Roboto:wght@400;500;700&family=Montserrat:wght@800&display=swap">
<style>
  :root {
    --stage: #3b3b3b;
    --brand-red: #e00000;
    --paper: #ffffff;
    --arc-grey: #a9a9ae;
    --ink-light: #ffffff;
  }
  * { margin: 0; padding: 0; box-sizing: border-box; }
  html, body { width: 1200px; height: 900px; overflow: hidden; }
  body {
    background: radial-gradient(circle at 50% 45%, #555 0%, var(--stage) 70%);
    font-family: "Roboto", Arial, sans-serif;
    position: relative;
  }
  .card {
    position: absolute;
    left: 300px;
    width: 600px;
    height: 343px;
    overflow: hidden;
    box-shadow: 0 14px 30px rgba(0,0,0,.45);
  }
  .card--front { top: 70px; background: var(--brand-red); }
  .card--contact { top: 480px; background: var(--brand-red); }

  .wordmark {
    font-family: "Montserrat", Arial, sans-serif;
    font-weight: 800;
    letter-spacing: 1px;
    white-space: nowrap;
  }
  .card--front .wordmark {
    position: absolute;
    left: 0; right: 0; top: 120px;
    text-align: center;
    font-size: 46px;
    color: var(--ink-light);
  }
  .card--front .web {
    position: absolute;
    left: 0; right: 0; top: 210px;
    text-align: center;
    font-size: 15px;
    color: var(--ink-light);
    letter-spacing: .5px;
  }

  .contact-block {
    position: absolute;
    left: 40px; top: 38px;
    color: var(--ink-light);
  }
  .contact-block .person {
    font-size: 24px; font-weight: 500; letter-spacing: .5px;
  }
  .contact-block .role {
    font-size: 14px; margin-top: 2px; opacity: .92;
  }
  .contact-block .address {
    margin-top: 20px; font-size: 15px; line-height: 1.4;
  }
  .contact-list {
    list-style: none; margin-top: 10px; font-size: 15px; line-height: 1.55;
  }
  .contact-list li { display: flex; align-items: center; gap: 8px; }
  .contact-list svg { width: 12px; height: 12px; fill: var(--ink-light); flex: none; }

  .badge-arc {
    position: absolute; left: 0; top: 0; width: 600px; height: 343px;
  }
  .card--contact .wordmark {
    position: absolute;
    left: 340px; top: 150px;
    width: 200px;
    text-align: center;
    font-size: 34px;
    line-height: 1.1;
    color: var(--brand-red);
  }
</style>
</head>
<body>

<section class="card card--front" aria-label="Card front">
  <div class="wordmark">ALPINE COUNSEL</div>
  <div class="web">www.alpinecounsel.com</div>
</section>

<section class="card card--contact" aria-label="Card back with contact details">
  <svg class="badge-arc" viewBox="0 0 600 343" aria-hidden="true">
    <circle cx="500" cy="300" r="232" fill="none" stroke="var(--arc-grey)" stroke-width="6"/>
    <circle cx="505" cy="305" r="228" fill="var(--paper)"/>
  </svg>

  <div class="contact-block">
    <div class="person">DANIEL REYES</div>
    <div class="role">Director</div>
    <div class="address">1187 Harlow Ridge<br>Salem, OR 97301</div>
    <ul class="contact-list">
      <li><svg viewBox="0 0 24 24"><path d="M6.6 10.8a15.1 15.1 0 0 0 6.6 6.6l2.2-2.2a1 1 0 0 1 1-.25 11.4 11.4 0 0 0 3.6.57 1 1 0 0 1 1 1V20a1 1 0 0 1-1 1A17 17 0 0 1 3 4a1 1 0 0 1 1-1h3.5a1 1 0 0 1 1 1c0 1.25.2 2.45.57 3.6a1 1 0 0 1-.25 1z"/></svg>555 014-2290</li>
      <li><svg viewBox="0 0 24 24"><path d="M2 5h20v14H2zm2 2v.5l8 5 8-5V7zm0 2.8V17h16V9.8l-8 5z"/></svg>info@alpinecounsel.com</li>
      <li><svg viewBox="0 0 24 24"><path d="M12 2a10 10 0 1 0 0 20 10 10 0 0 0 0-20zm6.9 6h-3a15.6 15.6 0 0 0-1.4-3.6A8 8 0 0 1 18.9 8zM12 4a14 14 0 0 1 1.9 4h-3.8A14 14 0 0 1 12 4zM4.3 14a8 8 0 0 1 0-4h3.4a16.5 16.5 0 0 0 0 4zm.8 2h3a15.6 15.6 0 0 0 1.4 3.6A8 8 0 0 1 5.1 16zm3-8h-3a8 8 0 0 1 4.4-3.6A15.6 15.6 0 0 0 8.1 8zM12 20a14 14 0 0 1-1.9-4h3.8A14 14 0 0 1 12 20zm2.3-6H9.7a14.7 14.7 0 0 1 0-4h4.6a14.7 14.7 0 0 1 0 4zm.2 5.6a15.6 15.6 0 0 0 1.4-3.6h3a8 8 0 0 1-4.4 3.6zm1.8-5.6a16.5 16.5 0 0 0 0-4h3.4a8 8 0 0 1 0 4z"/></svg>www.alpinecounsel.com</li>
    </ul>
  </div>

  <div class="wordmark">ALPINE<br>COUNSEL</div>
</section>

</body>
</html>
```